Larkvale Gastroenterology business cards, stationary and envelopes
Larkvale Gastroenterology business cards, stationary and envelopes - Medical
Creative Brief
Simple
Dorian Velmoretti, M.D.
Gastroenterology And Liver Disease (and under it) Clinical Nutrition
17 West 63rd, Suite 4C New York, NY 10342
dorianvelm@quillbox.net
www.pinwardclinic.com
Would like professional, stylish business card (front and back), envelopes and full stationary package required. Front card should be white bacground. please see my website www.pinwardclinic.com
I am open to ideas, possibly just the website and logo

```html
<!DOCTYPE html>
<html lang="en">
<head>
<meta charset="utf-8">
<title>Larkvale Gastroenterology Stationery</title>
<link href="https://fonts.googleapis.com/css2?family=Cinzel:wght@400;600&family=Open+Sans:wght@400;600&display=swap" rel="stylesheet">
<style>
:root{
  --bg-dark:#2b2b2b;
  --bg-mid:#4a4a4a;
  --paper:#ffffff;
  --ink:#1a1a1a;
  --grey:#9a9a9a;
  --soft:#e6e6e6;
  --faint:#ececec;
  --black:#111111;
}
*{margin:0;padding:0;box-sizing:border-box}
html,body{width:1200px;height:382px;overflow:hidden}
body{background:radial-gradient(ellipse at 30% 40%,var(--bg-mid),var(--bg-dark) 75%);position:relative;font-family:"Open Sans",sans-serif;color:var(--ink)}
.brand{position:absolute;display:flex;align-items:center;gap:8px}
.brand-dot{border-radius:50%;background:var(--paper);flex:none}
.brand-name{font-family:"Cinzel",serif;font-weight:600;text-transform:uppercase;line-height:1.05;white-space:nowrap}
.hero-brand{left:40px;top:132px}
.hero-brand .brand-dot{width:38px;height:38px}
.hero-brand .brand-name{color:var(--paper);font-size:15px}
.hero-caption{position:absolute;left:86px;top:180px;color:#bbb;font-size:8px}
.card{position:absolute;width:144px;height:64px;box-shadow:0 2px 5px rgba(0,0,0,.6);overflow:hidden}
.card.light{background:var(--paper)}
.card.dark{background:var(--black);color:var(--paper)}
.card .brand{left:10px;top:14px;gap:4px}
.card .brand-dot{width:16px;height:16px;background:var(--ink)}
.card.dark .brand-dot{background:var(--paper)}
.card .brand-name{font-size:7px}
.card.dark .brand-name{color:var(--paper)}
.card-url{position:absolute;left:10px;bottom:6px;font-size:4px;color:var(--grey)}
.card-details{position:absolute;right:8px;top:10px;text-align:right;font-size:4.2px;line-height:1.5}
.card-details strong{font-size:5.5px;display:block;margin-bottom:2px}
.card-band{position:absolute;left:0;right:0;bottom:0;height:9px;background:var(--soft)}
.letterhead{position:absolute;top:12px;width:284px;height:360px;background:var(--paper);box-shadow:0 3px 8px rgba(0,0,0,.6);overflow:hidden}
.letterhead .brand{left:18px;top:20px;gap:5px}
.letterhead .brand-dot{width:20px;height:20px;background:var(--ink)}
.letterhead .brand-name{font-size:8px}
.lh-contact{position:absolute;right:18px;top:20px;font-size:4.5px;line-height:1.6;color:#555;text-align:left}
.lh-mark{position:absolute;left:62px;top:100px;width:160px;height:160px;border-radius:50%;background:var(--faint)}
.lh-footer{position:absolute;left:0;bottom:0;width:100%;height:40px}
.lh-footnote{position:absolute;left:0;right:0;bottom:4px;text-align:center;font-size:4px;color:#ccc}
.envelope{position:absolute;left:936px;width:252px;height:106px;background:var(--paper);box-shadow:0 2px 6px rgba(0,0,0,.6);overflow:hidden}
.envelope svg{position:absolute;left:0;top:0}
.envelope .brand{left:14px;top:60px;gap:4px}
.envelope .brand-dot{width:16px;height:16px;background:var(--ink)}
.envelope .brand-name{font-size:7px}
.env-url{position:absolute;left:0;right:0;bottom:5px;text-align:center;font-size:4px;color:var(--grey)}
</style>
</head>
<body>

<div class="brand hero-brand">
  <span class="brand-dot"></span>
  <span class="brand-name">Larkvale<br>Gastroenterology</span>
</div>
<p class="hero-caption">Stationery Concept</p>

<div class="card light" style="left:12px;top:233px">
  <div class="brand"><span class="brand-dot"></span><span class="brand-name">Larkvale<br>Gastroenterology</span></div>
  <p class="card-url">www.pinwardclinic.com</p>
</div>
<div class="card light" style="left:161px;top:233px">
  <div class="card-details">
    <strong>Dorian Velmoretti, M.D.</strong>
    Gastroenterology And Liver Disease<br>Clinical Nutrition<br>
    17 West 63rd, Suite 4C<br>New York, NY 10342<br>
    dorianvelm@quillbox.net
  </div>
  <div class="card-band"></div>
</div>
<div class="card dark" style="left:12px;top:307px">
  <div class="brand"><span class="brand-dot"></span><span class="brand-name">Larkvale<br>Gastroenterology</span></div>
  <p class="card-url">www.pinwardclinic.com</p>
</div>
<div class="card dark" style="left:161px;top:307px">
  <div class="card-details">
    <strong>Dorian Velmoretti, M.D.</strong>
    Gastroenterology And Liver Disease<br>Clinical Nutrition<br>
    17 West 63rd, Suite 4C<br>New York, NY 10342<br>
    www.pinwardclinic.com
  </div>
</div>

<div class="letterhead" style="left:324px">
  <div class="brand"><span class="brand-dot"></span><span class="brand-name">Larkvale<br>Gastroenterology</span></div>
  <div class="lh-contact">17 West 63rd, Suite 4C<br>New York, NY 10342<br>Tel (212) 555-0148<br>dorianvelm@quillbox.net</div>
  <div class="lh-mark"></div>
  <svg class="lh-footer" viewBox="0 0 284 40" preserveAspectRatio="none">
    <path d="M0 18 Q140 2 284 20 L284 40 L0 40Z" fill="#cfcfcf"/>
    <path d="M0 26 Q140 12 284 28 L284 40 L0 40Z" fill="#111"/>
  </svg>
  <p class="lh-footnote">www.pinwardclinic.com</p>
</div>
<div class="letterhead" style="left:630px">
  <div class="lh-mark"></div>
  <svg class="lh-footer" viewBox="0 0 284 40" preserveAspectRatio="none">
    <path d="M0 18 Q140 2 284 20 L284 40 L0 40Z" fill="#cfcfcf"/>
    <path d="M0 26 Q140 12 284 28 L284 40 L0 40Z" fill="#111"/>
  </svg>
  <p class="lh-footnote">17 West 63rd, Suite 4C · New York, NY 10342 · www.pinwardclinic.com</p>
</div>

<div class="envelope" style="top:18px">
  <svg width="252" height="106" viewBox="0 0 252 106"><path d="M0 0 L126 52 L252 0Z" fill="#d4d4d4"/></svg>
</div>
<div class="envelope" style="top:106px">
  <svg width="252" height="106" viewBox="0 0 252 106"><path d="M0 0 L126 50 L252 0Z" fill="#111"/></svg>
</div>
<div class="envelope" style="top:200px">
  <svg width="252" height="106" viewBox="0 0 252 106"><path d="M0 0 L126 24 L252 0Z" fill="#e2e2e2"/></svg>
  <div class="brand" style="top:32px"><span class="brand-dot"></span><span class="brand-name">Larkvale<br>Gastroenterology</span></div>
</div>
<div class="envelope" style="top:272px">
  <div class="brand" style="top:14px"><span class="brand-dot"></span><span class="brand-name">Larkvale<br>Gastroenterology</span></div>
  <p class="env-url">www.pinwardclinic.com</p>
</div>

</body>
</html>
```